Online Home Automation business needs business card design

New business starting up that sells home-automation products in Australia. Business card needs to look very polished and professional. The business name is "Finch Automation".
Updates

Thank you all for the great designs, We are really impressed. We are in the process of deciding on a design but keep the designs coming in.

Industry/Entity Type

Business

```html
<!DOCTYPE html>
<html lang="en">
<head>
<meta charset="utf-8">
<title>Finch Automation – Business Card</title>
<link rel="stylesheet" href="https://fonts.googleapis.com/css2?family=Questrial&family=Nunito+Sans:wght@700&family=Roboto+Condensed:wght@400&display=swap">
<style>
  :root {
    --page: #ffffff;
    --ink: #111111;
    --brand-red: #e41b1b;
    --swoosh: #e6e6e6;
    --band-light: #fbfbfb;
    --band-mid: #e2e2e2;
    --card-border: #222222;
  }
  * { margin: 0; padding: 0; box-sizing: border-box; }
  html, body { width: 915px; height: 1200px; overflow: hidden; background: var(--page); }
  body { position: relative; font-family: "Questrial", sans-serif; color: var(--ink); }

  .side-label {
    position: absolute; left: 0; width: 915px; text-align: center;
    font-family: Arial, Helvetica, sans-serif; font-size: 38px; color: #000;
  }
  .side-label.front { top: 128px; left: -10px; }
  .side-label.back { top: 1022px; }

  .card {
    position: absolute; left: 115px; width: 684px; height: 391px;
    border: 1px solid var(--card-border); background: var(--page); overflow: hidden;
  }
  .card.front { top: 177px; }
  .card.back { top: 630px; }

  .card-art { position: absolute; inset: 0; width: 684px; height: 391px; }

  .brand { position: absolute; display: flex; align-items: center; }
  .brand-dot { border-radius: 50%; background: var(--ink); flex: none; }
  .brand-name { color: var(--ink); line-height: 0.95; font-weight: 400; }

  .card.front .brand { left: 276px; top: 29px; gap: 20px; }
  .card.front .brand-dot { width: 98px; height: 98px; }
  .card.front .brand-name { font-size: 46px; }

  .card.back .brand { left: 414px; top: 34px; gap: 16px; }
  .card.back .brand-dot { width: 70px; height: 70px; }
  .card.back .brand-name { font-size: 33px; }

  .holder-name { position: absolute; left: 16px; top: 25px; font-size: 22px; }

  .specialization { position: absolute; left: 17px; top: 315px; }
  .specialization-title {
    font-family: "Nunito Sans", sans-serif; font-weight: 700; font-size: 20px;
    letter-spacing: 1.5px; text-decoration: underline; text-underline-offset: 3px;
  }
  .specialization-text { margin-top: 7px; font-size: 19px; }
  .specialization-text .accent { color: var(--brand-red); }

  .country {
    position: absolute; right: 10px; bottom: 14px;
    font-family: "Roboto Condensed", sans-serif; font-size: 25px;
    color: var(--brand-red); letter-spacing: -0.5px;
  }
  .card.back .country { right: 14px; bottom: 14px; }

  .contact { position: absolute; left: 23px; top: 312px; list-style: none; font-size: 15px; line-height: 20px; }
</style>
</head>
<body>
  <div class="side-label front">FRONT</div>

  <section class="card front">
    <svg class="card-art" viewBox="0 0 684 391" aria-hidden="true">
      <defs>
        <linearGradient id="band-front" x1="0" x2="1" y1="0" y2="0">
          <stop offset="0" stop-color="var(--band-light)"/>
          <stop offset="0.25" stop-color="var(--band-mid)"/>
          <stop offset="1" stop-color="var(--band-light)"/>
        </linearGradient>
      </defs>
      <path d="M146 78 L202 27 H684 V129 H202 Z" fill="url(#band-front)"/>
      <path d="M0 391 V380 C150 290 300 200 403 148 C300 210 250 320 330 368 C380 392 500 391 550 391 Z" fill="var(--swoosh)"/>
    </svg>
    <div class="holder-name">Mara Ellis</div>
    <div class="brand">
      <span class="brand-dot"></span>
      <span class="brand-name">Finch<br>Automation</span>
    </div>
    <div class="specialization">
      <div class="specialization-title">SPECIALIZATION</div>
      <div class="specialization-text"><span class="accent">ONLINE</span> Selling Home Automation Products.</div>
    </div>
    <div class="country">AUSTRALIA</div>
  </section>

  <section class="card back">
    <svg class="card-art" viewBox="0 0 684 391" aria-hidden="true">
      <defs>
        <linearGradient id="band-back" x1="0" x2="1" y1="0" y2="0">
          <stop offset="0" stop-color="var(--band-light)"/>
          <stop offset="0.25" stop-color="var(--band-mid)"/>
          <stop offset="1" stop-color="var(--band-light)"/>
        </linearGradient>
      </defs>
      <path d="M290 69 L335 31 H684 V107 H335 Z" fill="url(#band-back)"/>
      <path d="M0 391 V380 C150 290 300 200 403 148 C300 210 250 320 330 368 C380 392 500 391 550 391 Z" fill="var(--swoosh)"/>
    </svg>
    <div class="brand">
      <span class="brand-dot"></span>
      <span class="brand-name">Finch<br>Automation</span>
    </div>
    <ul class="contact">
      <li>Tel :- +61 400 555 019</li>
      <li>Website :- www.finchautomation.com.au</li>
      <li>E-mail :- info@finchautomation.com.au</li>
    </ul>
    <div class="country">AUSTRALIA</div>
  </section>

  <div class="side-label back">BACK</div>
</body>
</html>
```